Quirky Business Card Design

Business card:
A quirky card for a professional audience

Business:
A professional consultancy offering corporate training and coaching

I've attached my sketches and happy for you to shapen the design and/or add your own ideas.

Front of card (see file 2 below):
Card must be easy for client to find among many
A bit quirky – implies that it needs thought, needs orientation
White card, black high gloss letters

Arrows:
One spot colour – fresh amber-orange, but not fluro nor candy colour
A colour that is not feminine nor masculine; old nor young
Meant to represent the amber of traffic lights
? black outline
Arrows oriented left to right and bottom to top i.e. headed in the right direction
May need to work in a straight line for header or footer or invoices (see file 3 below)

Back of card (e.g. in file 1):
Very clean and easy to read
Preferred fonts: I like the aesthetic of Century Gothic but with “a”.
Copy to include:
Plunge Ahead Now
Harriet Dunmore
t: +61 (0)412 907 263
e: harriet@plungeaheadnow.com
w: www.plungeaheadnow.com

May use the by-line “Making the remarkable happen”

I am looking for a web page design in the future so I am looking to be delighted!!
Updates

Dear Designers,

I would like the copy at the back of the card to include the registered business number: 

ABN: 8213 605 4479

Many thanks,

Harriet.

Industry/Entity Type

Training

```html
<!DOCTYPE html>
<html lang="en">
<head>
<meta charset="utf-8">
<title>Plunge Ahead Now — Business Card</title>
<link rel="stylesheet" href="https://fonts.googleapis.com/css2?family=Poppins:wght@400;600;800&display=swap">
<style>
  :root {
    --backdrop: #1b1b1b;
    --card-white: #ffffff;
    --card-back: #f1f1f1;
    --ink: #000000;
    --ink-name: #4a4a4a;
    --ink-soft: #7a7a7a;
    --amber: #e8ac3a;
  }
  * { box-sizing: border-box; margin: 0; padding: 0; }
  html, body {
    width: 1200px;
    height: 871px;
    overflow: hidden;
    background: var(--backdrop);
    font-family: "Poppins", "Century Gothic", sans-serif;
  }
  .stage {
    position: relative;
    width: 1200px;
    height: 871px;
  }
  .card {
    position: absolute;
    top: 282px;
    width: 540px;
    height: 307px;
    border: 14px solid var(--ink);
    border-radius: 4px;
    overflow: hidden;
  }

  /* Back of card */
  .card--back {
    left: 40px;
    background: var(--card-back);
    color: var(--ink-soft);
  }
  .card--back .holder-name {
    position: absolute;
    top: 18px;
    right: 26px;
    font-size: 28px;
    font-weight: 600;
    color: var(--ink-name);
  }
  .card--back .contact-phone {
    position: absolute;
    top: 66px;
    left: 24px;
    font-size: 20px;
  }
  .card--back .contact-web {
    position: absolute;
    top: 96px;
    right: 26px;
    list-style: none;
    text-align: right;
    font-size: 17px;
    line-height: 1.5;
  }
  .card--back .abn {
    position: absolute;
    top: 158px;
    right: 26px;
    font-size: 13px;
    letter-spacing: 0.04em;
  }
  .card--back .brand-name {
    position: absolute;
    right: 26px;
    bottom: 58px;
    font-size: 19px;
    font-weight: 800;
    color: var(--ink);
  }
  .card--back .byline {
    position: absolute;
    left: 24px;
    right: 26px;
    bottom: 20px;
    font-size: 12px;
    letter-spacing: 0.55em;
    text-align: right;
    color: #444;
  }

  /* Front of card */
  .card--front {
    left: 620px;
    background: var(--card-white);
    border-width: 18px;
  }
  .card--front .brand-name {
    position: absolute;
    left: 24px;
    top: 10px;
    font-size: 80px;
    font-weight: 800;
    line-height: 0.98;
    letter-spacing: -0.02em;
    color: var(--ink);
  }
  .card--front .brand-name span { display: block; }
  .card--front .brand-name .line-2 { padding-left: 70px; }
  .card--front .brand-name .line-3 { padding-left: 150px; }
  .card--front .brand-mark {
    position: absolute;
    right: 30px;
    bottom: 34px;
    width: 56px;
    height: 56px;
    background: var(--amber);
  }
</style>
</head>
<body>
<main class="stage">
  <section class="card card--back" aria-label="Back of business card">
    <p class="holder-name">Harriet Dunmore</p>
    <p class="contact-phone">+61 (0)412 907 263</p>
    <ul class="contact-web">
      <li>harriet@plungeaheadnow.com</li>
      <li>www.plungeaheadnow.com</li>
    </ul>
    <p class="abn">ABN: 8213 605 4479</p>
    <p class="brand-name">Plunge Ahead Now</p>
    <p class="byline">Making the remarkable happen.</p>
  </section>

  <section class="card card--front" aria-label="Front of business card">
    <p class="brand-name">
      <span class="line-1">Plunge</span>
      <span class="line-2">Ahead</span>
      <span class="line-3">Now</span>
    </p>
    <span class="brand-mark" aria-hidden="true"></span>
  </section>
</main>
</body>
</html>
```